Meridale Cleaning Services

In need of a business card design suited for a growing cleaning company.

We offer our cleaning and maintenance services to a wide range of clients including but not limited to the following: constuction industry, hospitality, commercial, industrial and domestic

I want the card to be very noticable, i would like people to say 'hey, great card!' when i hand them my card.double sided would be nice

we want our business to come across as exceedingly professional and innovative (different).

a contemporary design is what we have in mind
we want to present an image of a quality business with a high standard of excellence in consistent service.

i just really need a card that persuades top end quality,
our business is very certified and also strives towards environmentaly friendly alternatives
Updates

hey sorry, i have uploaded my company logo design and name
cheers.

hey guys i have added my company logo/name file on my brief page. many thanks

sorry guys a typo in the brief..
address is Tolley Rd. not Tolly Rd
thanks

Industry/Entity Type

Industrial

Requirements
Must have
• company name: meridale cleaning services
operations manager: Colm Varetti
Tel: (02)9373 6204
Fax: (02)8645 7712
Mob: 0438571490

address: 47 Tolly RD Pymble NSW 2073
Postal Adress: PO Box 5832 North Ryde NSW 2113
email: meridaleclean@wexanet.com.au
website: meridalecleaningservices.com.au

```html
<!DOCTYPE html>
<html lang="en">
<head>
<meta charset="utf-8">
<title>Meridale Cleaning Services – Business Card</title>
<link rel="stylesheet" href="https://fonts.googleapis.com/css2?family=Arimo:wght@400;700&display=swap">
<style>
  :root {
    --stage: #2e3236;
    --card: #ffffff;
    --card-shade: #eef1f4;
    --brand-blue: #1d5fb6;
    --band-blue: #1b9ad8;
    --band-cyan: #2ccdf4;
    --mist-blue: #9fd3f0;
    --type-white: #ffffff;
    --web-blue: #2a6fb5;
    --mark: #2c8fd6;
  }
  * { box-sizing: border-box; margin: 0; padding: 0; }
  html, body { width: 1200px; height: 814px; overflow: hidden; }
  body {
    background: var(--stage);
    font-family: "Arimo", Arial, sans-serif;
    position: relative;
  }
  .card {
    position: absolute;
    top: 257px;
    width: 520px;
    height: 300px;
    border-radius: 18px;
    background: radial-gradient(ellipse at 50% 40%, var(--card) 55%, var(--card-shade) 100%);
    box-shadow: 0 14px 34px rgba(0,0,0,.45);
    overflow: hidden;
  }
  .card--back { left: 60px; }
  .card--front { left: 620px; }

  .mist {
    position: absolute; left: 0; top: 0; width: 100%; height: 72px;
    background: linear-gradient(170deg, var(--mist-blue) 0%, rgba(159,211,240,.45) 45%, rgba(255,255,255,0) 100%);
  }

  .brand { position: absolute; display: flex; align-items: center; color: var(--brand-blue); font-weight: 700; }
  .brand__dot { border-radius: 50%; background: var(--mark); flex: none; }
  .brand__name { line-height: 1; }
  .brand__sub { display: block; letter-spacing: .3px; }

  .card--back .brand { left: 40px; top: 76px; gap: 10px; }
  .card--back .brand__dot { width: 40px; height: 40px; }
  .card--back .brand__name { font-size: 30px; }
  .card--back .brand__sub { font-size: 10px; margin-top: 2px; }

  .band {
    position: absolute; left: 0; top: 128px; width: 100%; height: 136px;
    background: linear-gradient(to bottom, var(--band-cyan) 0 18px, var(--band-blue) 18px);
    color: var(--type-white);
    padding: 26px 0 0 70px;
  }
  .contact__name { font-size: 16px; font-weight: 700; letter-spacing: .4px; }
  .contact__role { font-size: 11px; margin-bottom: 4px; }
  .contact__line { font-size: 11px; line-height: 13px; }
  .contact__address { font-size: 8px; line-height: 10px; margin-top: 4px; }

  .website {
    position: absolute; left: 0; top: 276px; width: 100%;
    text-align: center; font-size: 9px; letter-spacing: 4px; color: var(--web-blue);
  }

  .card--front .brand { left: 50%; top: 50%; transform: translate(-50%, -50%); gap: 14px; }
  .card--front .brand__dot { width: 58px; height: 58px; }
  .card--front .brand__name { font-size: 40px; }
  .card--front .brand__sub { font-size: 13px; margin-top: 3px; }
</style>
</head>
<body>
  <section class="card card--back" aria-label="Business card, contact side">
    <div class="mist" role="img" aria-label="Soft blue water texture"></div>
    <div class="brand">
      <span class="brand__dot"></span>
      <span class="brand__name">Meridale<span class="brand__sub">CLEANING SERVICES</span></span>
    </div>
    <div class="band">
      <p class="contact__name">COLM VARETTI</p>
      <p class="contact__role">operations manager</p>
      <p class="contact__line">Tel: (02)9373 6204</p>
      <p class="contact__line">Fax: (02)8645 7712</p>
      <p class="contact__line">Mob: 0438571490</p>
      <p class="contact__line">Email: meridaleclean@wexanet.com.au</p>
      <p class="contact__address">47 Tolley RD Pymble NSW 2073<br>PO Box 5832 North Ryde NSW 2113</p>
    </div>
    <p class="website">meridalecleaningservices.com.au</p>
  </section>

  <section class="card card--front" aria-label="Business card, brand side">
    <div class="brand">
      <span class="brand__dot"></span>
      <span class="brand__name">Meridale<span class="brand__sub">CLEANING SERVICES</span></span>
    </div>
  </section>
</body>
</html>
```